Banners for Website and Social Media

Technology Consulting and Services company requires several banners that integrate our logo that can be used on a basic website that we are designing. The design will also be used on social media platforms. Require a variety of sizes and shapes to be included. Need at least two variations for a website header, more variations will put you at the top of the leaderboard.

Target Market(s)

Non-Profit Mental Health Agencies, small business

Font styles to use
Serif

Requirements
Must have
• Show the idea of connecting with our clients. We require the following approximate sizes, they do not have to be exact:

2 x variations 1080px x 600px for website header
1 x 1128px x 191px for Brindlepost
1 x 590px x 175px for Email Marketing
1 x 300px x 250px for Advertising

Colours should compliment the logo that has been provided.
Nice to have
• Could integrate key words and phrases in the graphic but not standout as a tagline or title.

- Engaged
- Ethical Technology
- Support
- Connected
Should not have
• Banner should avoid having people in it. Prefer a more abstract feel.

```html
<!DOCTYPE html>
<html lang="en">
<head>
<meta charset="utf-8">
<title>Bridgewell Technology Partners – Banner Set</title>
<link rel="stylesheet" href="https://fonts.googleapis.com/css2?family=Inter:wght@300;400;600;700;800&family=Nunito:wght@700;800&display=swap">
<style>
  :root{
    --sheet:#e3eaf2;
    --navy:#0a1a7a;
    --royal:#0b35c9;
    --deep:#07155c;
    --violet:#5b1fc9;
    --purple:#3a1896;
    --cyan:#1fa8ff;
    --sky:#3fc4ff;
    --white:#ffffff;
    --soft:#dfe8ff;
  }
  *{box-sizing:border-box;margin:0;padding:0}
  html,body{width:1200px;height:673px;overflow:hidden;background:var(--sheet)}
  body{position:relative;font-family:"Inter",Arial,sans-serif;color:var(--white)}
  .banner{position:absolute;overflow:hidden}
  .abs{position:absolute}
  .art{position:absolute}
  .caps{text-transform:uppercase;font-weight:700;letter-spacing:.01em;white-space:nowrap}

  /* 1 — header, icons on right */
  .header-icons{left:96px;top:71px;width:449px;height:225px;
    background:radial-gradient(ellipse at 20% 70%,#0a2aa8 0%,var(--navy) 55%,#0c2fb8 100%)}
  .header-icons .art{right:0;top:0;width:240px;height:225px;
    background:radial-gradient(ellipse at 70% 50%,rgba(40,170,255,.45),rgba(20,80,230,.15) 60%,transparent 80%)}
  .header-icons h1{left:22px;top:74px;font-weight:300;font-size:18.5px;line-height:20px;letter-spacing:.01em}
  .header-icons .sub{left:22px;top:120px;font-size:9.6px;font-weight:300}
  .point{position:absolute;display:flex;align-items:center;gap:4px}
  .point .dot{width:28px;height:28px;border-radius:50%;background:var(--white);box-shadow:0 0 6px rgba(120,190,255,.8)}
  .point span{font-size:7px;font-weight:600;line-height:8px;text-transform:uppercase}

  /* 2 — header, centered name */
  .header-center{left:96px;top:313px;width:455px;height:236px;
    background:linear-gradient(180deg,#06215a 0%,#0a3c8e 60%,#0a4aa6 100%)}
  .header-center .art{left:40px;top:105px;width:375px;height:131px;
    background:radial-gradient(ellipse at 50% 55%,rgba(40,180,255,.65),rgba(20,110,230,.25) 55%,transparent 75%)}
  .header-center h1{left:0;width:100%;top:17px;text-align:center;font-family:"Nunito",Arial,sans-serif;font-weight:800;font-size:19px}
  .header-center .sub{left:0;width:100%;top:43px;text-align:center;font-family:"Nunito",Arial,sans-serif;font-weight:700;font-size:12px}
  .header-center .lbl{font-size:8px;font-family:"Nunito",Arial,sans-serif;font-weight:800;text-transform:uppercase}

  .name-mark{position:absolute;border-radius:50%;border:4px solid var(--cyan);display:flex;align-items:center;justify-content:center;font-weight:700;color:var(--cyan)}

  /* 3 — wide profile banner */
  .profile-wide{left:578px;top:71px;width:507px;height:154px;
    background:linear-gradient(90deg,#4a18b8 0%,#2a1a9a 45%,#0d2aa8 100%)}
  .profile-wide .art-l{left:0;top:0;width:140px;height:154px;background:radial-gradient(ellipse at 40% 50%,rgba(170,90,255,.45),transparent 70%)}
  .profile-wide .art-r{right:0;top:0;width:150px;height:154px;background:radial-gradient(ellipse at 60% 45%,rgba(40,170,255,.5),transparent 70%)}
  .profile-wide h1{left:0;width:100%;top:11px;text-align:center;font-size:15px;font-weight:700}
  .profile-wide .lbl{font-size:6px;font-weight:700;line-height:7px;text-transform:uppercase}

  /* small banners */
  .email-globe{left:586px;top:249px;width:213px;height:63px;background:linear-gradient(90deg,#0a1450,#101e6a 50%,#0a1450)}
  .email-globe .art{left:73px;top:8px;width:70px;height:60px;border-radius:50%;
    background:radial-gradient(circle at 50% 60%,#1a6fd0 0%,#5a2ab0 45%,#d0603a 70%,transparent 72%)}
  .email-globe h2{left:0;width:100%;top:5px;text-align:center;font-size:6.3px}
  .email-globe .lbl{font-size:2.8px;font-weight:700;text-transform:uppercase}
  .ring{position:absolute;width:12px;height:12px;border-radius:50%;border:1px solid var(--cyan)}

  .email-lines{left:586px;top:328px;width:213px;height:63px;background:linear-gradient(90deg,#0b1a6a,#0a1e72 60%,#0c2a8a)}
  .email-lines .art{right:0;top:0;width:90px;height:63px;background:radial-gradient(ellipse at 60% 50%,rgba(60,150,255,.35),transparent 70%)}
  .email-lines h2{left:10px;top:10px;font-size:8.6px}
  .email-lines .sub{left:10px;top:22px;font-size:6.5px;font-weight:300}

  .email-orb{left:586px;top:413px;width:213px;height:62px;background:linear-gradient(90deg,#1c2aa8,#2a1eaa 60%,#4a18b8)}
  .email-orb .art{left:105px;top:0;width:108px;height:62px;background:radial-gradient(ellipse at 50% 50%,#8a3af0 0%,#5a22d0 45%,rgba(60,30,190,0) 75%)}
  .email-orb h2{left:12px;top:13px;font-size:7.5px;line-height:10px}

  .ticks{position:absolute;display:grid;grid-template-columns:auto auto;column-gap:12px;row-gap:6px}
  .tick{display:flex;align-items:center;gap:3px;font-size:4.6px;font-weight:700;text-transform:uppercase;white-space:nowrap}
  .tick::before{content:"";width:5px;height:5px;border:.7px solid var(--white);border-radius:50%;
    background:linear-gradient(45deg,transparent 45%,var(--white) 46%,var(--white) 56%,transparent 57%)}

  .ad-head{left:839px;top:249px;width:145px;height:121px;background:linear-gradient(120deg,#1a2aa0,#3a1ea8 60%,#4a1aa0)}
  .ad-head .art{right:0;top:0;width:90px;height:121px;background:radial-gradient(ellipse at 60% 45%,rgba(150,110,255,.5),transparent 70%)}
  .ad-head h2{left:13px;top:19px;font-size:12.6px;line-height:14px}

  .ad-center{left:839px;top:392px;width:145px;height:121px;background:linear-gradient(160deg,#1838c0,#2a2ab8 55%,#4a1ea8)}
  .ad-center .art{left:0;top:0;width:145px;height:121px;background:radial-gradient(ellipse at 70% 30%,rgba(80,160,255,.35),transparent 60%)}
  .ad-center .t{left:0;width:100%;text-align:center;white-space:nowrap}
</style>
</head>
<body>

<!-- Website header 1 -->
<section class="banner header-icons">
  <div class="art" role="img" aria-label="Glowing blue circuit-board trace pattern"></div>
  <h1 class="abs">BRIDGEWELL TECHNOLOGY<br>PARTNERS</h1>
  <p class="abs sub">Technology Consulting and Services</p>
  <div class="point" style="left:259px;top:16px"><i class="dot"></i><span>Ethical<br>Technology</span></div>
  <div class="point" style="left:290px;top:74px"><i class="dot"></i><span>Connected</span></div>
  <div class="point" style="left:259px;top:132px"><i class="dot"></i><span>Support</span></div>
  <div class="point" style="left:307px;top:182px"><i class="dot"></i><span>Engaged</span></div>
</section>

<!-- Website header 2 -->
<section class="banner header-center">
  <div class="art" role="img" aria-label="Glowing concentric holographic rings"></div>
  <h1 class="abs">Bridgewell Technology Partners</h1>
  <p class="abs sub">Technology Consulting and Services</p>
  <svg class="abs" style="left:0;top:0" width="455" height="236" viewBox="0 0 455 236">
    <g fill="none" stroke="#cfe6ff" stroke-width="1">
      <polyline points="123,94 143,80 190,80"/>
      <polyline points="332,94 312,80 265,80"/>
      <polyline points="123,166 143,180 190,180"/>
      <polyline points="332,166 312,180 265,180"/>
    </g>
    <g fill="#fff"><circle cx="123" cy="94" r="2.5"/><circle cx="332" cy="94" r="2.5"/><circle cx="123" cy="166" r="2.5"/><circle cx="332" cy="166" r="2.5"/></g>
  </svg>
  <span class="abs lbl" style="left:77px;top:86px">Engaged</span>
  <span class="abs lbl" style="left:340px;top:85px">Support</span>
  <span class="abs lbl" style="left:26px;top:162px">Ethical Technology</span>
  <span class="abs lbl" style="left:340px;top:161px">Connected</span>
  <div class="name-mark" style="left:178px;top:78px;width:100px;height:100px;font-size:13px">Bridgewell</div>
</section>

<!-- Brindlepost profile banner -->
<section class="banner profile-wide">
  <div class="art art-l" role="img" aria-label="Violet circuit trace pattern"></div>
  <div class="art art-r" role="img" aria-label="Blue circuit trace pattern"></div>
  <h1 class="abs caps">BRIDGEWELL TECHNOLOGY PARTNERS</h1>
  <div class="name-mark" style="left:186px;top:39px;width:112px;height:112px;border-color:#7a7cff;color:#8a8cff;font-size:15px">Bridgewell</div>
  <span class="abs lbl" style="left:134px;top:59px">Support</span>
  <span class="abs lbl" style="left:316px;top:55px">Ethical<br>Technology</span>
  <span class="abs lbl" style="left:124px;top:121px">Connected</span>
  <span class="abs lbl" style="left:318px;top:121px">Engaged</span>
  <svg class="abs" style="left:0;top:0" width="507" height="154" viewBox="0 0 507 154">
    <g fill="none" stroke="#fff" stroke-width="1.4">
      <circle cx="196" cy="58" r="2.6"/><circle cx="287" cy="58" r="2.6"/>
      <circle cx="193" cy="124" r="2.6"/><circle cx="289" cy="124" r="2.6"/>
    </g>
  </svg>
</section>

<!-- Email banner A -->
<section class="banner email-globe">
  <div class="art" role="img" aria-label="Glowing globe with colourful halo"></div>
  <h2 class="abs caps">BRIDGEWELL TECHNOLOGY PARTNERS</h2>
  <span class="abs" style="left:85px;top:28px;font-size:8px;font-weight:700;color:var(--sky)">Bridgewell</span>
  <span class="abs lbl" style="left:47px;top:26px">Support</span><i class="ring" style="left:65px;top:23px"></i>
  <span class="abs lbl" style="left:36px;top:48px">Connected</span><i class="ring" style="left:58px;top:44px"></i>
  <i class="ring" style="left:143px;top:23px"></i><span class="abs lbl" style="left:158px;top:25px">Ethical<br>Technology</span>
  <i class="ring" style="left:150px;top:44px"></i><span class="abs lbl" style="left:165px;top:47px">Engaged</span>
</section>

<!-- Email banner B -->
<section class="banner email-lines">
  <div class="art" role="img" aria-label="Network of connected lines and nodes"></div>
  <h2 class="abs caps">BRIDGEWELL TECHNOLOGY PARTNERS</h2>
  <p class="abs sub">Technology Consulting and Services</p>
  <div class="ticks" style="left:12px;top:38px">
    <span class="tick">Support</span><span class="tick">Connected</span>
    <span class="tick">Engaged</span><span class="tick">Ethical Technology</span>
  </div>
</section>

<!-- Email banner C -->
<section class="banner email-orb">
  <div class="art" role="img" aria-label="Violet faceted glow behind the name"></div>
  <h2 class="abs caps">BRIDGEWELL TECHNOLOGY<br>PARTNERS</h2>
  <div class="ticks" style="left:12px;top:39px">
    <span class="tick">Support</span><span class="tick">Connected</span>
    <span class="tick">Engaged</span><span class="tick">Ethical Technology</span>
  </div>
  <div class="name-mark" style="left:128px;top:8px;width:48px;height:48px;border:3px solid var(--white);color:var(--white);font-size:7.5px">Bridgewell</div>
</section>

<!-- Advertising A -->
<section class="banner ad-head">
  <div class="art" role="img" aria-label="Abstract violet digital glow"></div>
  <h2 class="abs caps">BRIDGEWELL<br>TECHNOLOGY<br>PARTNERS</h2>
  <div class="ticks" style="left:16px;top:66px;row-gap:7px;column-gap:10px">
    <span class="tick">Support</span><span class="tick">Connected</span>
    <span class="tick">Engaged</span><span class="tick">Ethical Technology</span>
  </div>
</section>

<!-- Advertising B -->
<section class="banner ad-center">
  <div class="art" role="img" aria-label="Soft blue circuit trace glow"></div>
  <div class="name-mark" style="left:62px;top:11px;width:21px;height:21px;border:1.5px solid var(--soft);color:var(--soft);font-size:3.6px">Bridgewell</div>
  <p class="abs t caps" style="top:34px;font-size:14px;line-height:14px">BRIDGEWELL</p>
  <p class="abs t caps" style="top:48px;font-size:14px;line-height:14px">TECHNOLOGY</p>
  <p class="abs t" style="top:62px;font-size:10.5px;font-weight:300;line-height:12px">PARTNERS</p>
  <div class="ticks" style="left:16px;top:85px;row-gap:8px;column-gap:14px">
    <span class="tick">Support</span><span class="tick">Connected</span>
    <span class="tick">Engaged</span><span class="tick">Ethical Technology</span>
  </div>
</section>

</body>
</html>
```